new KVR one page flyer

We need a 1 page A4 size flyer (need it asap please) that describes on 1 page with art work and using photos the services we provide. I have included some examples of old previous flyers from our other (seperate divisions of the business) I have named a photo called (photo for top of design) however you do your design this photo needs to be the star of the page by either having it at the top or bottom of the page please and we usually like this photo to be in greyscale colour.
we do like greyscale designs but are open to see what you come up with as a whole page of grey white and black might not suit.

Needs to list the following

Services include:
Over size loads / Hot Shot Loads
Heavy Vehicle Recovery services
Potable Water Deliveries
Road Building / Maintenance
Earthworks
Sand & Metal Supply & Cartage
Road Train Tippers
Road Train Tankers
Road Train Flat Tops
Drop Deck Trailers
Mine site accredited equipment & Operators.

We offer a large rage of services not listed so call us today for a personalised quote to suit your needs.

To go on the bottom of the page our contact details are

KVR Pty Ltd
Depot: Lot 514, Banksia Flats Track Coober Pedy
Mobile: 047 216 9381
email: darren@kestrelvaleroadworks.com.au

Target Market(s)

new clients

Colors

Designer to choose colors to be used in the design.

Requirements
Must have
• our services listed
Nice to have
• stand out designs

```html
<!DOCTYPE html>
<html lang="en">
<head>
<meta charset="utf-8">
<title>KVR Services Flyer</title>
<link rel="stylesheet" href="https://fonts.googleapis.com/css2?family=Oswald:wght@500;600;700&family=Roboto:wght@400;500&display=swap">
<style>
  :root {
    --yellow: #fdb913;
    --ink: #1f1f1f;
    --charcoal: #2e2e2e;
    --footer: #1c1c1c;
    --paper: #ffffff;
    --backdrop: #d4d4d4;
    --text: #2a2a2a;
  }
  * { margin: 0; padding: 0; box-sizing: border-box; }
  html, body { width: 1200px; height: 1200px; overflow: hidden; background: var(--backdrop); }
  .canvas { position: relative; width: 1200px; height: 1200px; }
  .flyer {
    position: absolute; left: 194px; top: 30px;
    width: 925px; height: 1297px;
    transform: scale(0.879); transform-origin: 0 0;
    background: var(--paper); overflow: hidden;
    font-family: "Roboto", Arial, sans-serif; color: var(--text);
  }
  .abs { position: absolute; }
  .top-band { left: 0; top: 0; }
  .hero { left: 0; top: 27px; }
  .brand {
    left: 0; width: 925px; top: 40px; text-align: center;
    font-family: "Oswald", sans-serif; font-weight: 700; font-size: 104px;
    line-height: 1; color: var(--ink); letter-spacing: 4px;
  }
  .feature-photo { left: 462px; top: 489px; }
  .photo { background: linear-gradient(180deg, #a9bcd0 0%, #cfd4d8 42%, #b98a66 62%, #a8694a 100%); }
  .photo-a { left: 462px; top: 846px; width: 194px; height: 120px; }
  .photo-b { left: 660px; top: 846px; width: 247px; height: 172px; background: linear-gradient(180deg, #b5bfca 0%, #d3d5d5 45%, #b8946f 65%, #a98160 100%); }
  .photo-c { left: 462px; top: 970px; width: 194px; height: 233px; background: linear-gradient(180deg, #7ea3d3 0%, #dfe4e8 38%, #c4895a 62%, #b8713f 100%); }
  .photo-d { left: 660px; top: 1022px; width: 247px; height: 181px; background: linear-gradient(180deg, #6f98d0 0%, #cbd6e0 35%, #a28670 58%, #a9764f 100%); }
  .offer-tag {
    left: 45px; top: 598px; height: 49px; padding: 0 16px 0 5px;
    background: var(--yellow); color: var(--ink);
    font-size: 44px; line-height: 49px; font-weight: 500;
  }
  .offer-headline {
    left: 50px; top: 648px;
    font-family: "Oswald", sans-serif; font-weight: 600; font-size: 58px;
    line-height: 62px; color: var(--yellow); letter-spacing: 0.5px;
  }
  .services-title {
    left: 60px; top: 802px;
    font-family: "Oswald", sans-serif; font-weight: 600; font-size: 35px;
    line-height: 48px; color: var(--ink);
  }
  .services-title .accent { color: var(--yellow); }
  .services-title .marker { display: inline-block; width: 7px; height: 30px; vertical-align: -3px; margin-right: 8px;
    background: linear-gradient(180deg, var(--yellow) 0 35%, var(--ink) 35% 100%); }
  .service-list { left: 62px; top: 866px; list-style: none; }
  .service-list li {
    position: relative; padding-left: 20px;
    font-size: 18px; line-height: 27.2px; color: var(--text);
  }
  .service-list li::before {
    content: ""; position: absolute; left: 0; top: 9px;
    width: 10px; height: 10px; border-radius: 50%; background: var(--yellow);
  }
  .service-list li .wrap { display: block; line-height: 22px; }
  .footer { left: 0; top: 1208px; width: 925px; height: 89px; background: var(--footer); color: #fff; }
  .contact { position: absolute; display: flex; align-items: center; gap: 12px; font-size: 16px; line-height: 20px; }
  .contact-depot { left: 36px; top: 22px; }
  .contact-email { left: 384px; top: 25px; }
  .contact-phone { left: 728px; top: 22px; }
</style>
</head>
<body>
<div class="canvas">
  <article class="flyer">
    <svg class="abs top-band" width="925" height="27" viewBox="0 0 925 27">
      <rect width="925" height="27" fill="var(--yellow)"/>
      <polygon points="0,0 536,0 526,27 0,27" fill="var(--charcoal)"/>
    </svg>

    <svg class="abs hero" width="925" height="540" viewBox="0 0 925 540" role="img" aria-label="Greyscale photo of a road train with two tipper trailers on an outback dirt track">
      <defs>
        <linearGradient id="heroTone" x1="0" y1="0" x2="0" y2="1">
          <stop offset="0" stop-color="#e4dfdd"/>
          <stop offset="0.3" stop-color="#bdb5b2"/>
          <stop offset="0.58" stop-color="#6e6664"/>
          <stop offset="0.78" stop-color="#8f8785"/>
          <stop offset="1" stop-color="#a29a98"/>
        </linearGradient>
        <radialGradient id="heroShade" cx="0.45" cy="0.62" r="0.6">
          <stop offset="0" stop-color="#3a3433" stop-opacity="0.35"/>
          <stop offset="1" stop-color="#3a3433" stop-opacity="0"/>
        </radialGradient>
      </defs>
      <path d="M0 0 H925 V452 Q640 540 440 532 Q200 525 0 510 Z" fill="url(#heroTone)"/>
      <path d="M0 0 H925 V452 Q640 540 440 532 Q200 525 0 510 Z" fill="url(#heroShade)"/>
    </svg>

    <div class="abs brand">KVR</div>

    <svg class="abs feature-photo" width="445" height="354" viewBox="0 0 445 354" role="img" aria-label="Photo of a black prime mover pulling water tanker trailers on red earth under blue sky">
      <defs>
        <linearGradient id="featureTone" x1="0" y1="0" x2="0" y2="1">
          <stop offset="0" stop-color="#3f77c6"/>
          <stop offset="0.4" stop-color="#93b3db"/>
          <stop offset="0.6" stop-color="#7c6a63"/>
          <stop offset="0.75" stop-color="#b86f47"/>
          <stop offset="1" stop-color="#a85d38"/>
        </linearGradient>
      </defs>
      <path d="M0 73 Q230 55 445 0 V354 H0 Z" fill="url(#featureTone)"/>
    </svg>

    <div class="abs photo photo-a" role="img" aria-label="Photo of a truck hauling transportable buildings along a dirt road"></div>
    <div class="abs photo photo-b" role="img" aria-label="Photo of a flat top trailer loaded with earthmoving machinery"></div>
    <div class="abs photo photo-c" role="img" aria-label="Photo of a truck carrying an oversize tank on red outback ground"></div>
    <div class="abs photo photo-d" role="img" aria-label="Photo of two prime movers parked beside a curved steel shed"></div>

    <div class="abs offer-tag">WE OFFER</div>
    <h1 class="abs offer-headline">A LARGE RANGE<br>OF SERVICES</h1>

    <h2 class="abs services-title"><span class="marker"></span><span class="accent">SERVICES</span> INCLUDE</h2>
    <ul class="abs service-list">
      <li>Over size loads / Hot Shot Loads</li>
      <li>Heavy Vehicle Recovery services</li>
      <li>Potable Water Deliveries</li>
      <li>Road Building / Maintenance</li>
      <li>Earthworks</li>
      <li>Sand &amp; Metal Supply &amp; Cartage</li>
      <li>Road Train Tippers</li>
      <li>Road Train Tankers</li>
      <li>Road Train Flat Tops</li>
      <li>Drop Deck Trailers</li>
      <li><span class="wrap">Mine site accredited equipment<br>&amp; Operators.</span></li>
    </ul>

    <footer class="abs footer">
      <div class="contact contact-depot">
        <svg width="34" height="36" viewBox="0 0 34 36" aria-hidden="true">
          <path d="M17 2a9 9 0 0 0-9 9c0 7 9 16 9 16s9-9 9-16a9 9 0 0 0-9-9zm0 12.5a3.5 3.5 0 1 1 0-7 3.5 3.5 0 0 1 0 7z" fill="var(--yellow)"/>
          <ellipse cx="17" cy="30" rx="15" ry="4" fill="none" stroke="var(--yellow)" stroke-width="2"/>
        </svg>
        <span>Depot: Lot 514,<br>Banksia Flats Track Coober Pedy</span>
      </div>
      <div class="contact contact-email">
        <svg width="30" height="18" viewBox="0 0 30 18" aria-hidden="true">
          <rect x="1" y="1" width="28" height="16" fill="var(--yellow)"/>
          <path d="M1 1 L15 11 L29 1" fill="none" stroke="var(--footer)" stroke-width="2"/>
        </svg>
        <span>darren@kestrelvaleroadworks.com.au</span>
      </div>
      <div class="contact contact-phone">
        <svg width="18" height="36" viewBox="0 0 18 36" aria-hidden="true">
          <path d="M6 2 L11 2 L12 9 L8 11 Q7 18 10 25 L14 26 L16 33 L11 34 Q3 27 2 17 Q2 8 6 2 Z" fill="var(--yellow)"/>
        </svg>
        <span>047 216 9381</span>
      </div>
    </footer>
  </article>
</div>
</body>
</html>
```